AI Discovery Workshop Presentation

We have a wireframe presentation with 43 slides (many with the same format) to be implemented in Powerpoint. We provide Corporate presentation in order to reuse template. Please, be creative and don't take the examples in the wireframe as literal. We also provide the following:
- Color palette
- bytefolk Logos
- Slide wireframe
- Flyer
- bytefolk Corporate Presentation. Please, use this as a general template.
You can find all the materials here:
https://files.vantorbox.net/share/7QmZp2LxR9dKw4TnB8yHc3VfJ5sEaU0?usp=sharing

```html
<!DOCTYPE html>
<html lang="en">
<head>
<meta charset="utf-8">
<title>bytefolk – Technology Pitch Deck, Slides 1-12</title>
<link rel="stylesheet" href="https://fonts.googleapis.com/css2?family=Poppins:ital,wght@0,300;0,400;0,500;0,600;0,700;0,800;1,600;1,700&display=swap">
<style>
:root{
  --sage:#a6bfa5;
  --ink:#0c2b3a;
  --deep:#0b2a40;
  --petrol:#0d4a55;
  --teal:#1fa69a;
  --teal-dark:#1d6b63;
  --mint:#e6f2ef;
  --paper:#ffffff;
  --grey:#f0f0f0;
  --muted:#6c7c80;
}
*{box-sizing:border-box;margin:0;padding:0}
html,body{width:1200px;height:1200px;overflow:hidden}
body{background:var(--sage);font-family:"Poppins",sans-serif;color:var(--ink);position:relative}
.slide{position:absolute;width:374px;height:210px;overflow:hidden;background:var(--paper)}
.abs{position:absolute}
.photo{position:absolute}
.logo{position:absolute;display:flex;align-items:center;gap:3px;font-weight:600;color:#fff;letter-spacing:-.2px}
.logo .sq{display:inline-block;background:var(--teal)}
.logo.dark{color:var(--ink)}
.footer-num{position:absolute;font-size:3.2px;color:#9aa;font-weight:600}
.footer-lbl{position:absolute;font-size:4px;color:var(--ink);font-weight:500}
.footer-line{position:absolute;height:.6px;background:var(--teal)}
.btn{position:absolute;border-radius:8px;font-size:4px;display:flex;align-items:center;justify-content:space-between;padding:0 3px 0 8px}
.btn .dot{width:7px;height:7px;border-radius:50%;display:inline-block}
.h-bold{font-weight:700;line-height:1}
.h-light{font-weight:300;line-height:1}
.teal{color:var(--teal)}
.small{font-size:4.4px;line-height:1.45}
ul.bullets{list-style:none}
ul.bullets li{position:relative;padding-left:5px;font-size:3.6px;line-height:1.9;color:var(--ink)}
ul.bullets li::before{content:"";position:absolute;left:0;top:3px;width:1.6px;height:1.6px;border-radius:50%;background:var(--teal)}
.caption{position:absolute;font-size:60px;font-weight:800;color:var(--teal-dark);letter-spacing:-2px;left:107px;top:1010px}
</style>
</head>
<body>

<!-- 1 Cover, photo -->
<section class="slide" style="left:24px;top:94px">
  <div class="photo" role="img" aria-label="Woman with glasses in neon tech light" style="inset:0;background:radial-gradient(circle at 62% 40%,#3b2b4e 0,#243447 35%,#1b4a50 65%,#1d6b63 100%)"></div>
  <div class="abs" style="right:20px;top:19px;font-size:4px;font-weight:600;color:#fff;display:flex;gap:14px"><span>Business Company</span><span>2024</span></div>
  <div class="logo" style="left:30px;top:28px;font-size:18px"><span class="sq" style="width:8px;height:8px"></span>bytefolk</div>
  <div class="abs h-bold" style="left:30px;top:58px;font-size:28px;color:#fff">Technology</div>
  <div class="abs h-light" style="left:30px;top:86px;font-size:28px;color:#fff">Pitch Deck</div>
  <div class="abs" style="left:34px;top:124px;font-size:7.5px;font-weight:700;color:#fff">Template By:</div>
  <div class="abs small" style="left:34px;top:133px;width:130px;color:#e4eeee;font-size:4.4px">Lorem Ipsum is simply dummy text of the printing and typesetting industry.</div>
  <div class="abs" style="left:34px;top:160px;width:310px;height:.6px;background:#8fb8b4"></div>
  <div class="btn" style="left:286px;top:173px;width:55px;height:14px;background:#fff;color:var(--ink)">Learn More<span class="dot" style="background:var(--teal)"></span></div>
</section>

<!-- 2 Cover, white with photo strips -->
<section class="slide" style="left:414px;top:94px">
  <div class="photo" role="img" aria-label="Pale fabric close-up" style="left:20px;top:22px;width:40px;height:166px;border-radius:20px;background:linear-gradient(160deg,#eee6dc,#a7947f)"></div>
  <div class="photo" role="img" aria-label="Team photo detail" style="left:-12px;top:56px;width:26px;height:100px;border-radius:13px;background:#8a6a55"></div>
  <svg class="abs" style="left:73px;top:40px" width="20" height="18" viewBox="0 0 20 18"><path d="M10 1v14M3 9l7 7 7-7" fill="none" stroke="#1fa69a" stroke-width="2"/></svg>
  <div class="abs h-bold" style="left:73px;top:66px;font-size:16px">Technology</div>
  <div class="abs h-light teal" style="left:75px;top:86px;font-size:13px;font-weight:400">Pitch Deck</div>
  <div class="abs" style="left:74px;top:119px;font-size:7px;font-weight:700;color:#555">Template By:</div>
  <div class="abs small" style="left:74px;top:128px;width:95px;font-size:4.4px;color:#888">Lorem Ipsum is simply dummy text of the printing and typesetting industry.</div>
  <div class="btn" style="left:73px;top:163px;width:55px;height:14px;background:var(--teal);color:#fff">Learn More<span class="dot" style="background:#fff"></span></div>
  <div class="photo" role="img" aria-label="Smiling colleagues at work" style="left:186px;top:50px;width:40px;height:110px;border-radius:20px;background:linear-gradient(#b38a6d,#6a4632)"></div>
  <div class="photo" role="img" aria-label="Smiling colleagues at work" style="left:229px;top:0;width:40px;height:177px;border-radius:0 0 20px 20px;background:linear-gradient(#3f2a20,#8b6248)"></div>
  <div class="photo" role="img" aria-label="Smiling colleagues at work" style="left:272px;top:10px;width:40px;height:200px;border-radius:20px 20px 0 0;background:linear-gradient(#c59b7a,#7b4f33)"></div>
  <div class="photo" role="img" aria-label="Smiling colleagues at work" style="left:314px;top:18px;width:40px;height:180px;border-radius:20px;background:linear-gradient(#d5c2ad,#8c6a4f)"></div>
  <div class="photo" role="img" aria-label="Smiling colleagues at work" style="left:356px;top:0;width:30px;height:160px;border-radius:0 0 15px 15px;background:#5b3b2b"></div>
</section>

<!-- 3 Cover, teal 2025 -->
<section class="slide" style="left:802px;top:94px;background:linear-gradient(120deg,#0e5a60,#0b2a40)">
  <div class="abs" style="right:-26px;top:10px;font-size:72px;font-weight:800;color:rgba(255,255,255,.08);writing-mode:vertical-rl;line-height:1">2025</div>
  <div class="logo" style="left:34px;top:28px;font-size:17px"><span class="sq" style="width:8px;height:8px"></span>bytefolk</div>
  <div class="abs h-bold" style="left:26px;top:66px;font-size:28px;color:#fff">Technology</div>
  <div class="abs h-light" style="left:30px;top:96px;font-size:28px;color:#fff">Pitch Deck</div>
  <div class="abs" style="left:30px;top:134px;font-size:7.5px;font-weight:700;color:#fff">Template By:</div>
  <div class="abs small" style="left:30px;top:143px;width:130px;color:#dfeaea;font-size:4.4px">Lorem Ipsum is simply dummy text of the printing and typesetting industry.</div>
  <div class="abs" style="left:26px;top:178px;width:87px;height:12px;border:.7px solid #7ea3aa;border-radius:7px;font-size:5.5px;letter-spacing:1.6px;color:#fff;display:flex;align-items:center;justify-content:center">www.brightdeck.com</div>
</section>

<!-- 4 Welcome -->
<section class="slide" style="left:24px;top:311px;background:#0d4a55">
  <div class="abs" style="inset:0 0 0 0;background:linear-gradient(120deg,#0f5b60,#0b2a40)"></div>
  <div class="abs" style="left:0;top:0;width:28px;height:210px;border-right:.6px solid #2e7a7c"></div>
  <svg class="abs" style="left:9px;top:8px" width="11" height="9"><path d="M0 1h11M0 4.5h11M0 8h11" stroke="#fff" stroke-width="1"/></svg>
  <svg class="abs" style="left:10px;top:54px" width="9" height="6"><path d="M0 5l4.5-4 4.5 4" fill="none" stroke="#9cc" stroke-width=".8"/></svg>
  <svg class="abs" style="left:10px;top:148px" width="9" height="6"><path d="M0 1l4.5 4 4.5-4" fill="none" stroke="#9cc" stroke-width=".8"/></svg>
  <div class="logo" style="left:54px;top:17px;font-size:11px"><span class="sq" style="width:5px;height:5px"></span>bytefolk</div>
  <div class="abs" style="right:14px;top:9px;font-size:3.6px;color:#fff;font-weight:600">Modern Style</div>
  <div class="abs h-bold" style="left:54px;top:52px;font-size:22px;color:#fff">Technology</div>
  <div class="abs h-light" style="left:57px;top:78px;font-size:13px;color:#fff;font-weight:400">Pitch Deck</div>
  <div class="abs" style="left:55px;top:100px;width:172px;height:.6px;background:#6a9aa0"></div>
  <div class="abs" style="left:56px;top:106px;font-size:4.4px;color:#fff">Template</div>
  <div class="abs" style="left:56px;top:119px;font-size:5.6px;color:#fff;line-height:1.3">Business<br>Presentation<br><span style="color:#7fb3b4">template.</span></div>
  <div class="abs" style="left:56px;top:151px;font-size:3.2px;color:#fff">Modern Design</div>
  <div class="abs" style="left:119px;top:143px;font-size:3.2px;color:#fff;line-height:1.2">Lorem ipsum<br>Dolor<br>Sit amet.</div>
  <div class="abs" style="left:166px;top:151px;font-size:3.6px;color:#fff">Premium <span style="color:#7fb3b4">Design</span></div>
  <div class="photo" role="img" aria-label="Woman with glasses in magenta neon light" style="left:232px;top:33px;width:106px;height:144px;background:linear-gradient(135deg,#d13a7a,#4a1d6a 55%,#1b1b45)"></div>
  <div class="abs" style="left:349px;top:79px;width:12px;height:9px;border:.7px solid #c38bd6;border-radius:2px;font-size:3px;color:#fff;display:flex;align-items:center;justify-content:center">01</div>
  <div class="abs" style="left:352px;top:96px;font-size:2.8px;color:#5c8c90;line-height:4.6">02<br>03<br>04</div>
  <div class="abs" style="left:36px;top:180px;font-size:3.2px;color:#fff;font-weight:600">01/ <span style="color:#7fa">39</span></div>
  <div class="abs" style="left:36px;top:187px;font-size:4px;color:#fff;font-weight:600">Welcome Slide</div>
  <div class="abs" style="left:36px;top:195px;width:58px;height:.8px;background:#d06a9a"></div>
  <div class="abs" style="right:14px;top:196px;font-size:3.6px;color:#fff;font-weight:600">bytefolk presentation</div>
</section>

<!-- 5 The future is now, quote -->
<section class="slide" style="left:414px;top:311px">
  <div class="abs h-bold" style="left:45px;top:18px;font-size:15px;line-height:.98">The<br>future <span class="teal">is</span><br><span class="teal">now</span></div>
  <div class="abs teal" style="left:44px;top:74px;font-size:14px;font-weight:800;line-height:1">“</div>
  <div class="abs" style="left:45px;top:84px;width:122px;font-size:6.5px;line-height:1.6;color:#333">Generative AI has the potential to add trillions of dollars in value to the global economy and accelerate productivity growth for individuals, businesses and the economy as a whole. <span class="teal" style="font-weight:800;font-size:10px">”</span></div>
  <div class="abs" style="left:45px;top:150px;font-size:4.4px;font-weight:600">— Harlow &amp; Pratt</div>
  <div class="abs" style="left:14px;top:172px;transform:rotate(-90deg);transform-origin:left top;font-size:7.5px;font-weight:700">bytefolk</div>
  <div class="abs" style="left:18px;top:187px;width:11px;height:11px;border-radius:50%;background:linear-gradient(135deg,#0b2a40,#1fa69a)"></div>
  <div class="photo" role="img" aria-label="Woman touching a holographic interface, greyscale" style="left:203px;top:18px;width:90px;height:93px;background:linear-gradient(135deg,#e0e0e0,#555)"></div>
  <div class="abs" style="left:293px;top:51px;width:53px;height:8px;background:linear-gradient(90deg,var(--teal),#e6f7f4)"></div>
  <div class="photo" role="img" aria-label="Business handshake with pen, greyscale" style="left:267px;top:82px;width:90px;height:93px;background:linear-gradient(135deg,#777,#1c1c1c)"></div>
  <div class="abs" style="left:267px;top:98px;width:32px;height:7px;background:var(--teal)"></div>
  <div class="photo" role="img" aria-label="Glass office tower, greyscale" style="left:174px;top:122px;width:82px;height:60px;background:linear-gradient(#888,#222)"></div>
  <div class="abs" style="left:131px;top:169px;width:44px;height:7px;background:linear-gradient(90deg,#e6f7f4,var(--teal))"></div>
  <div class="abs" style="left:256px;top:154px;width:21px;height:7px;background:var(--teal)"></div>
  <div class="footer-num" style="left:41px;top:186px">02/ 39</div>
  <div class="footer-lbl" style="left:41px;top:194px">About Company</div>
  <div class="footer-line" style="left:263px;top:197px;width:60px"></div>
  <div class="logo dark" style="left:327px;top:193px;font-size:6px"><span class="sq" style="width:3px;height:3px"></span>bytefolk</div>
</section>

<!-- 6 About us -->
<section class="slide" style="left:802px;top:311px">
  <div class="abs h-bold" style="left:30px;top:15px;font-size:13px">About <span class="teal">us</span></div>
  <div class="abs" style="left:25px;top:39px;width:324px;height:117px;background:linear-gradient(100deg,#0f5b60,#0b2a40);clip-path:polygon(0 0,94% 0,100% 14%,100% 100%,0 100%)"></div>
  <div class="abs" style="left:45px;top:55px;font-size:11px;font-weight:600;color:#fff;line-height:1.45">Data Analytics &amp; AI<br>for Nonconformists</div>
  <div class="abs" style="left:185px;top:60px;width:140px;font-size:3.4px;line-height:1.85;color:#dfeeee">We are a leading Professional Services company specialized in the design and implementation of cutting edge technologies in Cloud, Data Analytics &amp; AI.</div>
  <div class="photo" role="img" aria-label="Analytics dashboard screens with charts" style="left:100px;top:102px;width:264px;height:76px;background:linear-gradient(110deg,#0a1c2c,#15485c 60%,#1d6f86);clip-path:polygon(0 0,100% 0,100% 100%,12% 100%)"></div>
  <div class="footer-num" style="left:41px;top:186px">02/ 39</div>
  <div class="footer-lbl" style="left:41px;top:194px">About Company</div>
  <div class="footer-line" style="left:256px;top:197px;width:60px"></div>
  <div class="logo dark" style="left:320px;top:193px;font-size:6px"><span class="sq" style="width:3px;height:3px"></span>bytefolk</div>
</section>

<!-- 7 What we do, icons -->
<section class="slide" style="left:24px;top:527px;background:var(--grey)">
  <div class="abs" style="left:0;top:0;width:374px;height:122px;background:#050808"></div>
  <div class="photo" role="img" aria-label="Two business people viewing holographic AI charts" style="left:130px;top:0;width:244px;height:122px;background:linear-gradient(100deg,#0a1416,#0f4a55 55%,#1a8c94)"></div>
  <div class="abs h-bold" style="left:44px;top:36px;font-size:20px;color:#fff;line-height:1.3">What<br><span class="teal">we do</span></div>
  <div class="abs" style="left:0;top:102px;width:374px;display:flex;justify-content:space-around;padding:0 22px">
    <div style="width:86px;display:flex;flex-direction:column;align-items:center">
      <svg width="36" height="36" viewBox="0 0 36 36"><circle cx="18" cy="18" r="17" fill="#fff"/><circle cx="18" cy="18" r="14" fill="#1fa69a"/><circle cx="18" cy="14" r="3" fill="#fff"/><circle cx="12" cy="15" r="2.3" fill="#fff"/><circle cx="24" cy="15" r="2.3" fill="#fff"/><path d="M12 25c0-4 3-6 6-6s6 2 6 6zM7 24c0-3 2-5 5-5M29 24c0-3-2-5-5-5" fill="#fff"/></svg>
      <div style="font-size:7px;color:#444;margin-top:6px;text-align:center">Agentic AI</div></div>
    <div style="width:86px;display:flex;flex-direction:column;align-items:center">
      <svg width="36" height="36" viewBox="0 0 36 36"><circle cx="18" cy="18" r="17" fill="#fff"/><circle cx="18" cy="18" r="14" fill="#1fa69a"/><circle cx="18" cy="14" r="3.6" fill="#fff"/><path d="M11 26c0-5 3-7 7-7s7 2 7 7z" fill="#fff"/></svg>
      <div style="font-size:7px;color:#444;margin-top:6px;text-align:center">AI Agents</div></div>
    <div style="width:86px;display:flex;flex-direction:column;align-items:center">
      <svg width="36" height="36" viewBox="0 0 36 36"><circle cx="18" cy="18" r="17" fill="#fff"/><circle cx="18" cy="18" r="14" fill="#1fa69a"/><rect x="11" y="17" width="3" height="8" fill="#fff"/><rect x="16" y="12" width="3" height="13" fill="#fff"/><circle cx="23" cy="21" r="3.2" fill="none" stroke="#fff" stroke-width="1.5"/></svg>
      <div style="font-size:7px;color:#444;margin-top:2px;text-align:center;line-height:1.3">Advanced Analytics<br>&amp; ML</div></div>
    <div style="width:86px;display:flex;flex-direction:column;align-items:center">
      <svg width="36" height="36" viewBox="0 0 36 36"><circle cx="18" cy="18" r="17" fill="#fff"/><circle cx="18" cy="18" r="14" fill="#1fa69a"/><rect x="11" y="11" width="14" height="14" rx="2" fill="#fff"/><rect x="13.5" y="17" width="2" height="6" fill="#1fa69a"/><rect x="17" y="14" width="2" height="9" fill="#1fa69a"/><rect x="20.5" y="15.5" width="2" height="7.5" fill="#1fa69a"/></svg>
      <div style="font-size:7px;color:#444;margin-top:2px;text-align:center;line-height:1.3">Data Analytics &amp;<br>Visualization</div></div>
  </div>
  <div class="footer-num" style="left:41px;top:186px">02/ 39</div>
  <div class="footer-lbl" style="left:41px;top:194px">What we do</div>
  <div class="footer-line" style="left:266px;top:197px;width:60px"></div>
  <div class="logo dark" style="left:330px;top:193px;font-size:6px"><span class="sq" style="width:3px;height:3px"></span>bytefolk</div>
</section>

<!-- 8 What we do, stack diagram -->
<section class="slide" style="left:414px;top:527px;background:linear-gradient(135deg,#0e5a60,#0b2a40)">
  <div class="abs" style="left:5px;top:5px;width:364px;height:200px;border:.6px solid #2c6e74"></div>
  <div class="abs h-bold" style="left:21px;top:9px;font-size:13px;color:#fff">What <span class="teal">we do</span></div>
  <div class="abs" style="left:21px;top:27px;width:20px;height:146px;background:var(--teal)"></div>
  <div class="abs" style="left:25px;top:114px;transform:rotate(-90deg);transform-origin:left top;font-size:8.5px;color:#fff;font-weight:500">Talent</div>
  <div class="abs" style="left:341px;top:27px;width:20px;height:146px;background:var(--teal)"></div>
  <div class="abs" style="left:356px;top:63px;transform:rotate(90deg);transform-origin:left top;font-size:8.5px;color:#fff;font-weight:500">Methodology</div>
  <div class="abs" style="left:45px;top:27px;width:291px;height:37px;background:#fdfbf2"></div>
  <div class="abs" style="left:49px;top:34px;font-size:4.4px;font-weight:600">Activation</div>
  <div class="abs" style="left:94px;top:33px;width:53px;height:25px;background:var(--deep);color:#fff;font-size:4px;text-align:center;padding-top:13px;line-height:1.1">Agentic AI</div>
  <div class="abs" style="left:154px;top:33px;width:53px;height:25px;background:var(--deep);color:#fff;font-size:4px;text-align:center;padding-top:13px">AI Agents</div>
  <div class="abs" style="left:215px;top:33px;width:53px;height:25px;background:var(--teal);color:#fff;font-size:3.6px;text-align:center;padding-top:11px;line-height:1.2">Advanced<br>Analytics &amp; ML</div>
  <div class="abs" style="left:276px;top:33px;width:53px;height:25px;background:var(--teal);color:#fff;font-size:3.6px;text-align:center;padding-top:11px;line-height:1.2">Data Analytics<br>&amp; Visualization</div>
  <div class="abs" style="left:45px;top:65px;width:291px;height:28px;background:var(--mint)"></div>
  <div class="abs" style="left:49px;top:67px;font-size:4.4px;font-weight:600">Management</div>
  <div class="abs" style="left:109px;top:68px;width:45px;height:21px;border:.8px solid var(--ink);font-size:6.4px;display:flex;align-items:center;justify-content:center">APIs/Tool</div>
  <div class="abs" style="left:196px;top:79px;font-size:6.8px;font-weight:500">Models</div>
  <div class="abs" style="left:274px;top:79px;font-size:6.8px;font-weight:500">Data</div>
  <div class="abs" style="left:45px;top:94px;width:291px;height:28px;background:var(--mint)"></div>
  <div class="abs" style="left:49px;top:96px;font-size:4.4px;font-weight:600">Integration</div>
  <div class="abs" style="left:148px;top:109px;font-size:6.8px;font-weight:500">Connectors</div>
  <div class="abs" style="left:224px;top:109px;font-size:6.8px;font-weight:500">Data Ingestion</div>
  <div class="abs" style="left:45px;top:123px;width:291px;height:28px;background:var(--mint)"></div>
  <div class="abs teal" style="left:49px;top:125px;font-size:4.4px;font-weight:600">IT Assets</div>
  <div class="abs" style="left:144px;top:138px;font-size:6.8px;font-weight:500">Applications</div>
  <div class="abs" style="left:227px;top:138px;font-size:6.8px;font-weight:500">Data Source</div>
  <div class="abs" style="left:45px;top:153px;width:291px;height:20px;background:var(--teal);color:#fff;font-size:9.5px;font-weight:500;display:flex;align-items:center;justify-content:center">Technology</div>
  <div class="footer-num" style="left:39px;top:186px;color:#8bb">02/ 39</div>
  <div class="footer-lbl" style="left:39px;top:194px;color:#fff">What we do</div>
  <div class="footer-line" style="left:263px;top:197px;width:60px;background:#6a9aa0"></div>
  <div class="logo" style="left:327px;top:193px;font-size:6px"><span class="sq" style="width:3px;height:3px"></span>bytefolk</div>
</section>

<!-- 9 The future is now, photo grid -->
<section class="slide" style="left:802px;top:527px">
  <div class="photo" role="img" aria-label="Woman smiling at a meeting" style="left:14px;top:17px;width:103px;height:157px;border-radius:6px;background:linear-gradient(#b59476,#5e3f2d)"></div>
  <div class="photo" role="img" aria-label="Colleagues reviewing a tablet" style="left:121px;top:17px;width:76px;height:76px;border-radius:6px;background:linear-gradient(#a57c5c,#d6c4b0)"></div>
  <div class="photo" role="img" aria-label="Colleagues in a bright office" style="left:121px;top:97px;width:76px;height:77px;border-radius:6px;background:linear-gradient(#c3a387,#6a4a36)"></div>
  <div class="abs" style="left:163px;top:144px;width:119px;height:26px;border-radius:8px;background:var(--petrol)"></div>
  <div class="abs" style="left:172px;top:151px;font-size:3.8px;color:#fff">continuous learning investn</div>
  <div class="abs" style="left:259px;top:151px;font-size:3.8px;color:#fff">100%</div>
  <div class="abs" style="left:172px;top:161px;width:98px;height:1.6px;background:#5c8f95"></div>
  <div class="abs" style="left:172px;top:161px;width:76px;height:1.6px;background:#7fd8cf"></div>
  <div class="abs" style="left:245px;top:158px;width:7px;height:7px;border-radius:50%;background:#fff;border:1.4px solid var(--petrol)"></div>
  <div class="abs" style="left:291px;top:149px;font-size:11px;color:var(--ink)">3x <span style="font-size:4px;color:#666">market average</span></div>
  <div class="abs h-bold" style="left:208px;top:16px;font-size:16px;line-height:1.05">The future<br><span class="teal">is now</span></div>
  <div class="abs" style="left:208px;top:61px;font-size:3.6px;font-weight:600">Work with highly Motivated Trained and Committed Industry Professionals.</div>
  <div class="abs teal" style="left:208px;top:73px;font-size:3.6px;font-weight:600">How do we make it happen</div>
  <ul class="bullets abs" style="left:210px;top:81px">
    <li>Strict selection process</li><li>Competitive pay for premier talent</li><li>Exciting technologies and projects</li><li>100% certification target in 6 months</li><li>10% continuous learning investment (3x market average)</li><li>Culture that draws in the best professionals</li>
  </ul>
  <div class="footer-num" style="left:41px;top:186px">02/ 39</div>
  <div class="footer-lbl" style="left:41px;top:194px">What we do</div>
  <div class="footer-line" style="left:266px;top:197px;width:60px"></div>
  <div class="logo dark" style="left:330px;top:193px;font-size:6px"><span class="sq" style="width:3px;height:3px"></span>bytefolk</div>
</section>

<!-- 10 The future is now, diamonds -->
<section class="slide" style="left:24px;top:744px">
  <div class="photo" role="img" aria-label="Woman smiling, diamond crop" style="left:196px;top:-30px;width:90px;height:90px;transform:rotate(45deg);border-radius:10px;background:linear-gradient(#a98766,#e2d4c3)"></div>
  <div class="photo" role="img" aria-label="Woman at work, diamond crop" style="left:154px;top:43px;width:76px;height:76px;transform:rotate(45deg);border-radius:10px;background:linear-gradient(#cdb79d,#7a5a40)"></div>
  <div class="photo" role="img" aria-label="Coffee cup on desk, diamond crop" style="left:240px;top:43px;width:76px;height:76px;transform:rotate(45deg);border-radius:10px;background:linear-gradient(#b08664,#5c3f2c)"></div>
  <div class="photo" role="img" aria-label="Office detail, diamond crop" style="left:210px;top:118px;width:70px;height:70px;transform:rotate(45deg);border-radius:10px;background:linear-gradient(#7b5a44,#3e2a20)"></div>
  <div class="photo" role="img" aria-label="Hands on laptop, diamond crop" style="left:258px;top:164px;width:70px;height:70px;transform:rotate(45deg);border-radius:10px;background:linear-gradient(#d0a37e,#8a5f3f)"></div>
  <div class="abs h-bold" style="left:27px;top:21px;font-size:16px;line-height:1.05">The future<br><span class="teal">is now</span></div>
  <div class="abs" style="left:27px;top:55px;width:130px;font-size:3.8px;font-weight:600;line-height:1.5">Work with highly Motivated Trained and Committed Industry Professionals.</div>
  <div class="abs teal" style="left:27px;top:72px;font-size:3.8px;font-weight:600">How do we make it happen</div>
  <ul class="bullets abs" style="left:29px;top:81px">
    <li>Strict selection process</li><li>Competitive pay for premier talent</li><li>Exciting technologies and projects</li><li>100% certification target in 6 months</li><li>10% continuous learning investment (3x market average)</li><li>Culture that draws in the best professionals</li>
  </ul>
  <div class="logo dark" style="left:296px;top:132px;font-size:11px"><span class="sq" style="width:5px;height:5px"></span>bytefolk</div>
  <div class="abs" style="left:22px;top:141px;width:182px;height:35px;border-radius:4px;background:var(--petrol)"></div>
  <div class="abs" style="left:41px;top:146px;font-size:11px;color:#fff;font-weight:300">100%</div>
  <div class="abs" style="left:41px;top:160px;width:34px;font-size:3px;color:#cfe;text-align:center;line-height:1.4">certification<br>target</div>
  <div class="abs" style="left:89px;top:149px;font-size:14px;color:#fff;font-weight:300">3x <span style="font-size:8px">market average</span></div>
  <div class="footer-num" style="left:41px;top:186px">02/ 39</div>
  <div class="footer-lbl" style="left:41px;top:194px">What we do</div>
  <div class="footer-line" style="left:73px;top:196px;width:60px"></div>
</section>

<!-- 11 Outstanding Technologies -->
<section class="slide" style="left:414px;top:744px">
  <div class="abs h-bold" style="left:24px;top:26px;font-size:16px">Outstanding <span class="teal">Technologies</span></div>
  <div class="abs" style="left:70px;top:60px;width:233px;height:.6px;background:#bbb"></div>
  <div class="abs" style="left:70px;top:115px;width:233px;height:.6px;background:#bbb"></div>
  <div class="abs" style="left:70px;top:175px;width:233px;height:.6px;background:#bbb"></div>
  <div class="abs" style="left:188px;top:60px;width:.6px;height:55px;background:#bbb"></div>
  <div class="abs" style="left:159px;top:115px;width:.6px;height:60px;background:#bbb"></div>
  <div class="abs" style="left:78px;top:79px;width:20px;height:20px;border-radius:50%;background:#e8e8e8"></div>
  <div class="abs" style="left:104px;top:77px;font-size:9px;line-height:1.2">Meridian<br>AI Cloud Partner</div>
  <div class="abs" style="left:201px;top:79px;width:20px;height:20px;border-radius:50%;background:#e8e8e8"></div>
  <div class="abs" style="left:230px;top:77px;font-size:9px;line-height:1.2;color:#555">Skyline Cloud<br>Partner</div>
  <div class="abs" style="left:85px;top:121px;width:45px;height:48px;border-radius:3px;background:#13285a" role="img" aria-label="Partner badge"></div>
  <div class="abs" style="left:173px;top:136px;width:22px;height:22px;border-radius:50%;background:var(--ink)"></div>
  <div class="abs" style="left:203px;top:136px;font-size:14px;font-weight:500">LinkWeave</div>
  <div class="footer-num" style="left:41px;top:186px">02/ 39</div>
  <div class="footer-lbl" style="left:41px;top:194px">What we do</div>
  <div class="footer-line" style="left:266px;top:197px;width:60px"></div>
  <div class="logo dark" style="left:330px;top:193px;font-size:6px"><span class="sq" style="width:3px;height:3px"></span>bytefolk</div>
</section>

<!-- 12 Proven methodology -->
<section class="slide" style="left:802px;top:744px">
  <div class="abs h-bold" style="left:17px;top:16px;font-size:16px;line-height:1.05">Proven<br>Successful<br><span class="teal">Methodology</span></div>
  <div class="abs" style="left:15px;top:86px;font-size:48px;font-weight:800;color:var(--teal-dark);letter-spacing:-1.5px;line-height:1">500</div>
  <div class="abs teal" style="left:20px;top:141px;font-size:10.5px;font-weight:700;font-style:italic;line-height:1.3">Projects in Data<br>Analytics and Cloud</div>
  <div class="photo" role="img" aria-label="Woman in magenta neon light" style="left:146px;top:0;width:53px;height:46px;border-radius:0 0 6px 6px;background:linear-gradient(#2a1e3d,#b2306f)"></div>
  <div class="photo" role="img" aria-label="Woman in magenta neon light" style="left:146px;top:51px;width:53px;height:55px;border-radius:6px;background:linear-gradient(135deg,#6b2a7d,#d03b7a)"></div>
  <div class="photo" role="img" aria-label="Neon data network" style="left:203px;top:51px;width:53px;height:55px;border-radius:6px;background:linear-gradient(135deg,#3a1d50,#c23a6e)"></div>
  <div class="photo" role="img" aria-label="Woman in magenta neon light" style="left:146px;top:110px;width:53px;height:55px;border-radius:6px;background:linear-gradient(#4a1f62,#20143a)"></div>
  <div class="photo" role="img" aria-label="Neon data network" style="left:203px;top:110px;width:53px;height:55px;border-radius:6px;background:linear-gradient(#27173d,#7a2b6a)"></div>
  <div class="photo" role="img" aria-label="Woman in magenta neon light" style="left:203px;top:169px;width:53px;height:41px;border-radius:6px 6px 0 0;background:linear-gradient(#b2306f,#2a1e3d)"></div>
  <div class="abs" style="left:192px;top:99px;width:16px;height:16px;border-radius:50%;background:#fff;display:flex;align-items:center;justify-content:center"><span style="width:9px;height:9px;border-radius:50%;background:var(--ink);color:#fff;font-size:5px;display:flex;align-items:center;justify-content:center;font-weight:700">$</span></div>
  <div class="abs" style="left:221px;top:157px;width:16px;height:16px;border-radius:50%;background:#fff;display:flex;align-items:center;justify-content:center">
    <svg width="9" height="9" viewBox="0 0 10 10"><circle cx="5" cy="5" r="4.5" fill="#0c2b3a"/><path d="M5 5V.5A4.5 4.5 0 0 1 9.5 5z" fill="#fff"/></svg></div>
  <div class="abs" style="left:274px;top:18px;font-size:48px;font-weight:800;color:var(--teal-dark);letter-spacing:-1.5px;line-height:1">15</div>
  <div class="abs teal" style="left:277px;top:70px;font-size:13px;font-weight:700;font-style:italic;line-height:1.6">Years<br>Experience</div>
  <div class="footer-num" style="left:41px;top:186px">02/ 39</div>
  <div class="footer-lbl" style="left:41px;top:194px">What we do</div>
  <div class="footer-line" style="left:266px;top:197px;width:60px"></div>
  <div class="logo dark" style="left:330px;top:193px;font-size:6px"><span class="sq" style="width:3px;height:3px"></span>bytefolk</div>
</section>

<div class="caption">Slides: 1-12</div>

</body>
</html>
```